Book title: Wildflower: The gift of stillness!

This book is called: Wildflower: The gift of stillness!

A guide to understanding the most popular types of coaching and how to find the perfect coach for you.
The coaching industry has exploded over the past few years as the demand for them has increased. With so many different types of coaches it can be intimidating and overwhelming to find the perfect one for you. To further complicate matters, you may experience times in your life when you require multiple coaches. {Book Title} aims to quite the noise and assist you in finding the perfect coach for you. In this book, you will learn more about the different types of coaching as well as meet a hand-picked selection of coaches from the most popular coaching niches. Each featured coach has provided an exercise designed to move you powerfully forward. We encourage you to work through each exercise so you may experience firsthand the power of working with these incredible coaches.

We would like a professional and simple design. See examples included. We would like to see blood orange included in the design, please see color pallets included as well.

Target Market(s)

Corporate professionals wanting to explore the various types of coaching industry

Industry/Entity Type

Coaching - Health, business, spiritual

Font styles to use
Serif

Colors
EE7325
F08F49
F5BC92
FAE3D3
FDF4ED

Requirements
Must have
• Please include book title: Wildflower, Subtitle: The gift of stillness! Name of publishing company: Silver Lantern Publishing, Spaces for 8 author names on the front of the cover- Author Name
Nice to have
• A feminine yet corporate feel.
Should not have
• We don't want it

```html
<!DOCTYPE html>
<html lang="en">
<head>
<meta charset="utf-8">
<title>Wildflower: The gift of stillness!</title>
<link rel="stylesheet" href="https://fonts.googleapis.com/css2?family=Anton&family=Cinzel:wght@500;700&display=swap">
<style>
  :root {
    --sky-top: #f79c14;
    --sky-mid: #f8a04f;
    --horizon: #ee7325;
    --night: #16142a;
    --ink: #15142a;
    --outline: #ffffff;
    --author: #ffffff;
    --publisher: #fae3d3;
    --rule: #f08f49;
  }
  * { margin: 0; padding: 0; box-sizing: border-box; }
  html, body { width: 848px; height: 1200px; overflow: hidden; background: var(--night); }
  .cover {
    position: relative;
    width: 848px;
    height: 1200px;
    overflow: hidden;
  }
  .cover-photo {
    position: absolute;
    inset: 0;
    background:
      radial-gradient(ellipse 320px 260px at 460px 560px, rgba(250, 190, 140, 0.55), rgba(250, 190, 140, 0) 70%),
      linear-gradient(to bottom,
        var(--sky-top) 0%,
        var(--sky-top) 38%,
        var(--sky-mid) 50%,
        var(--horizon) 60%,
        #d9662a 63.5%,
        var(--night) 66%,
        #25203a 72%,
        var(--night) 78%,
        var(--night) 100%);
  }
  .title {
    position: absolute;
    top: 62px;
    left: 0;
    width: 100%;
    text-align: center;
    font-family: "Anton", "Arial Narrow", sans-serif;
    font-weight: 400;
    font-size: 142px;
    line-height: 1;
    letter-spacing: 1px;
    color: var(--ink);
    -webkit-text-stroke: 10px var(--outline);
    paint-order: stroke fill;
    text-transform: uppercase;
  }
  .subtitle {
    position: absolute;
    top: 228px;
    left: 0;
    width: 100%;
    text-align: center;
    font-family: "Cinzel", "Times New Roman", serif;
    font-weight: 700;
    color: var(--ink);
    -webkit-text-stroke: 6px var(--outline);
    paint-order: stroke fill;
    text-transform: uppercase;
    line-height: 1;
  }
  .subtitle-line { display: block; }
  .subtitle-line--first { font-size: 46px; }
  .subtitle-line--second { font-size: 44px; margin-top: 12px; }
  .authors {
    position: absolute;
    top: 850px;
    left: 40px;
    width: 768px;
    display: grid;
    grid-template-columns: 1fr 1fr;
    row-gap: 34px;
    list-style: none;
  }
  .author {
    text-align: center;
    font-family: "Cinzel", "Times New Roman", serif;
    font-weight: 500;
    font-size: 20px;
    line-height: 1;
    letter-spacing: 9px;
    padding-left: 9px;
    color: var(--author);
    text-transform: uppercase;
  }
  .publisher-rule {
    position: absolute;
    top: 1106px;
    left: 374px;
    width: 100px;
    height: 1px;
    background: var(--rule);
  }
  .publisher {
    position: absolute;
    top: 1128px;
    left: 0;
    width: 100%;
    text-align: center;
    font-family: "Cinzel", "Times New Roman", serif;
    font-weight: 500;
    font-size: 18px;
    letter-spacing: 6px;
    padding-left: 6px;
    color: var(--publisher);
    text-transform: uppercase;
  }
</style>
</head>
<body>
  <main class="cover">
    <div class="cover-photo" role="img" aria-label="Photograph: silhouette of a woman with a ponytail standing on rocks by the water, a city skyline across the bay against a glowing orange sunset sky"></div>
    <h1 class="title">Wildflower</h1>
    <h2 class="subtitle">
      <span class="subtitle-line subtitle-line--first">The Gift of</span>
      <span class="subtitle-line subtitle-line--second">Stillness!</span>
    </h2>
    <ul class="authors">
      <li class="author">Author Name</li>
      <li class="author">Author Name</li>
      <li class="author">Author Name</li>
      <li class="author">Author Name</li>
      <li class="author">Author Name</li>
      <li class="author">Author Name</li>
      <li class="author">Author Name</li>
      <li class="author">Author Name</li>
    </ul>
    <div class="publisher-rule"></div>
    <p class="publisher">Silver Lantern Publishing</p>
  </main>
</body>
</html>
```